Business card for Chicago based Private Equity Company

We need a business card for our PE company called Crestline Partners. We want a simple and clean, yet creative card design. The back side should reflect our logo. Also would like to see embossed ideas. Should reflect strength and growth. Our logo is attached. Also need editable file. Details are as follows for Business Card:

Dale Moravec Co-Founder 2750 Larkin Avenue Suite 410 Oak Brook, IL 60587 http://www.crestlinepartnersllc.example (D) 630.555.0142 (C) 312.555.0178 (E) dm@crestlinepartnersllc.example

```html
<!DOCTYPE html>
<html lang="en">
<head>
<meta charset="utf-8">
<title>Crestline Partners – Business Card</title>
<link href="https://fonts.googleapis.com/css2?family=Montserrat:wght@400;500;600&display=swap" rel="stylesheet">
<style>
  :root {
    --backdrop: #1c1a1a;
    --card-back: #111111;
    --card-front: #1e2120;
    --emboss: #2e2e2e;
    --ink: #f2f2f2;
    --ink-soft: #c9cccb;
  }
  * { box-sizing: border-box; margin: 0; padding: 0; }
  html, body { width: 1200px; height: 716px; overflow: hidden; }
  body {
    background: var(--backdrop);
    font-family: "Montserrat", sans-serif;
    position: relative;
  }
  .card {
    position: absolute;
    top: 215px;
    width: 500px;
    height: 286px;
    border-radius: 3px;
  }
  .card--back { left: 60px; background: var(--card-back); }
  .card--front { left: 640px; background: var(--card-front); color: var(--ink); }

  .wordmark {
    position: absolute;
    display: flex;
    align-items: center;
    gap: 12px;
    letter-spacing: 0.12em;
    font-weight: 500;
    text-transform: uppercase;
  }
  .wordmark__dot { flex: none; border-radius: 50%; }
  .card--back .wordmark {
    left: 50%; top: 50%; transform: translate(-50%, -50%);
    color: var(--emboss); font-size: 26px; white-space: nowrap;
  }
  .card--back .wordmark__dot { width: 46px; height: 46px; background: var(--emboss); }
  .card--front .wordmark {
    left: 40px; top: 34px; color: var(--ink); font-size: 19px;
  }
  .card--front .wordmark__dot { width: 34px; height: 34px; background: var(--ink); }

  .address {
    position: absolute; left: 40px; bottom: 52px;
    font-size: 11.5px; line-height: 1.6; color: var(--ink-soft);
  }
  .person {
    position: absolute; left: 282px; top: 132px;
  }
  .person__name { font-size: 17px; font-weight: 600; letter-spacing: 0.04em; text-transform: uppercase; }
  .person__role { font-size: 11.5px; color: var(--ink-soft); margin-top: 2px; }
  .contact {
    list-style: none; margin-top: 18px;
    font-size: 11.5px; line-height: 1.6; color: var(--ink-soft);
  }
  .contact b { color: var(--ink); font-weight: 600; margin-right: 4px; }
</style>
</head>
<body>
  <section class="card card--back" aria-label="Card back">
    <div class="wordmark"><span class="wordmark__dot"></span><span>Crestline Partners</span></div>
  </section>

  <section class="card card--front" aria-label="Card front">
    <div class="wordmark"><span class="wordmark__dot"></span><span>Crestline Partners</span></div>

    <address class="address" style="font-style:normal">
      2750 Larkin Avenue<br>
      Suite 410 Oak Brook, IL 60587<br>
      www.crestlinepartnersllc.example
    </address>

    <div class="person">
      <p class="person__name">Dale Moravec</p>
      <p class="person__role">Co-Founder</p>
      <ul class="contact">
        <li><b>[D]</b>630.555.0142</li>
        <li><b>[C]</b>312.555.0178</li>
        <li><b>[E]</b>dm@crestlinepartnersllc.example</li>
      </ul>
    </div>
  </section>
</body>
</html>
```